Psychology practice - information brochure/flyer - half A4 page folded (4 sides)

We need a brochure/flyer to market our psychology service to GPs (Doctors). We need to demonstrate to the doctors that we are the right choice for their patients, and that we cover a large range of services so all of their patients needs are met. We will demonstrate this by listing our range of services and our team of psychologists. We have two locations in Sydney and offer high end services. I've attached our company logo but we remain flexible regarding the style of the brochures. I will provide more details (services, locations & psychologist credentials) once our preferred brochure design has been selected.

```html
<!DOCTYPE html>
<html lang="en">
<head>
<meta charset="utf-8">
<title>Clear Path Psychology – Brochure Covers</title>
<link rel="stylesheet" href="https://fonts.googleapis.com/css2?family=Montserrat:wght@700;800&family=Open+Sans:wght@400;600&display=swap">
<style>
  :root {
    --gold: #f4b708;
    --gold-deep: #e49a00;
    --gold-soft: #f9d54a;
    --charcoal: #4a4b50;
    --charcoal-dark: #3c3d41;
    --paper: #ffffff;
    --meadow: #8fb83a;
    --meadow-light: #cfe08a;
    --stage: #e9e9e9;
  }
  html, body {
    margin: 0;
    padding: 0;
    width: 1200px;
    height: 791px;
    overflow: hidden;
    background: var(--stage);
  }
  .canvas {
    position: relative;
    width: 1200px;
    height: 791px;
    display: flex;
  }
  .cover {
    position: relative;
    width: 600px;
    height: 791px;
    overflow: hidden;
  }
  .cover svg { display: block; }
  .headline {
    font-family: "Montserrat", sans-serif;
    font-weight: 800;
    font-size: 25px;
    letter-spacing: 0.5px;
  }
  .brand-name {
    font-family: "Open Sans", sans-serif;
    font-weight: 400;
  }
  .contact-text {
    font-family: "Open Sans", sans-serif;
    font-weight: 400;
    font-size: 12.5px;
    fill: var(--paper);
  }
  .contact-lead {
    font-family: "Open Sans", sans-serif;
    font-weight: 600;
    font-size: 14px;
    fill: var(--paper);
  }
  .web-address {
    font-family: "Open Sans", sans-serif;
    font-size: 13px;
    fill: var(--paper);
    letter-spacing: 0.3px;
  }
  .tagline {
    font-family: "Open Sans", sans-serif;
    font-size: 9.5px;
    fill: #d9d9d9;
  }
</style>
</head>
<body>
<main class="canvas">

  <!-- Back cover -->
  <section class="cover cover--back">
    <svg width="600" height="791" viewBox="0 0 600 791">
      <defs>
        <radialGradient id="sunflowerGlow" cx="0.25" cy="0.35" r="0.8">
          <stop offset="0" stop-color="#f7c81c"/>
          <stop offset="0.45" stop-color="#f4d25a"/>
          <stop offset="1" stop-color="#e8e2c8"/>
        </radialGradient>
        <linearGradient id="goldPanel" x1="0" y1="0" x2="1" y2="1">
          <stop offset="0" stop-color="#f0b400"/>
          <stop offset="1" stop-color="#f6c52a"/>
        </linearGradient>
        <linearGradient id="meadowStrip" x1="0" y1="0" x2="0" y2="1">
          <stop offset="0" stop-color="#e4d49a"/>
          <stop offset="0.5" stop-color="#b9b877"/>
          <stop offset="1" stop-color="#7fae2e"/>
        </linearGradient>
      </defs>

      <rect class="backdrop" width="600" height="791" fill="url(#goldPanel)"/>

      <rect class="photo photo--sunflower" x="0" y="0" width="600" height="320" fill="url(#sunflowerGlow)"
            role="img" aria-label="Close-up photograph of a bright yellow sunflower against a soft sunny background"/>

      <rect class="photo photo--meadow" x="385" y="110" width="215" height="470" fill="url(#meadowStrip)"
            role="img" aria-label="Soft-focus photograph of a sunlit grassy meadow"/>

      <path class="panel panel--contact" d="M0 330 L385 168 L385 590 L0 620 Z" fill="url(#goldPanel)"/>
      <path class="divider" d="M0 335 L600 75" stroke="var(--paper)" stroke-width="4" fill="none"/>

      <g class="contact" transform="translate(48 420) rotate(-10)">
        <text class="contact-lead" x="0" y="0">To Make Appointments</text>
        <text class="contact-lead" x="0" y="18">Please Contact us on below</text>

        <g class="contact-row" transform="translate(0 48)">
          <rect x="0" y="-11" width="9" height="13" rx="2" fill="var(--paper)"/>
          <text class="contact-text" x="20" y="0">(02) 5550 0142</text>
        </g>
        <g class="contact-row" transform="translate(0 74)">
          <rect x="-1" y="-8" width="12" height="8" rx="1.5" fill="var(--paper)"/>
          <rect x="1.5" y="-12" width="7" height="4" fill="var(--paper)"/>
          <text class="contact-text" x="20" y="0">(02) 5550 0187</text>
        </g>
        <g class="contact-row" transform="translate(0 100)">
          <path d="M5 6 C0 0 -1 -3 -1 -5 A6 6 0 0 1 11 -5 C11 -3 10 0 5 6 Z" fill="var(--paper)"/>
          <circle cx="5" cy="-5" r="2" fill="var(--gold)"/>
          <text class="contact-text" x="20" y="-6">Suite 4, Level 2, 18 Linden Street</text>
          <text class="contact-text" x="20" y="10">Marrick NSW 2290</text>
        </g>
        <g class="contact-row" transform="translate(0 138)">
          <circle cx="5" cy="-4" r="6.5" fill="none" stroke="var(--paper)" stroke-width="1.8"/>
          <path d="M-1.5 -4 H11.5 M5 -10.5 V2.5" stroke="var(--paper)" stroke-width="1.3"/>
          <text class="contact-text" x="20" y="0">www.clearpathpsychology.com.au</text>
        </g>
        <g class="contact-row" transform="translate(0 162)">
          <rect x="-1" y="-9" width="13" height="9" fill="var(--paper)"/>
          <path d="M-1 -9 L5.5 -4 L12 -9" stroke="var(--gold)" stroke-width="1.2" fill="none"/>
          <text class="contact-text" x="20" y="0" style="font-size:10px">info@clearpathpsychology.com.au</text>
        </g>
      </g>

      <path class="band band--white" d="M0 640 C160 600 360 560 600 560 L600 578 C360 580 160 620 0 660 Z" fill="var(--paper)"/>
      <path class="footer" d="M0 660 C160 622 360 582 600 578 L600 791 L0 791 Z" fill="var(--charcoal)"/>
      <path class="band band--gold" d="M0 660 C160 622 360 582 600 578 L600 586 C360 592 160 632 0 676 Z" fill="var(--gold)"/>

      <g class="brand brand--back" transform="translate(265 728) rotate(-9)">
        <circle cx="-20" cy="-12" r="7" fill="var(--gold)"/>
        <text class="brand-name" x="-4" y="-16" font-size="26" fill="var(--paper)">Clear Path</text>
        <text class="brand-name" x="-4" y="10" font-size="20" fill="var(--paper)">Psychology</text>
        <line x1="-30" y1="24" x2="210" y2="24" stroke="#8a8b8f" stroke-width="0.8"/>
        <text class="tagline" x="-30" y="38">New location opening soon in Orchard St Marrick</text>
      </g>
    </svg>
  </section>

  <!-- Front cover -->
  <section class="cover cover--front">
    <svg width="600" height="791" viewBox="0 0 600 791">
      <defs>
        <linearGradient id="meadowScene" x1="0" y1="0" x2="0" y2="1">
          <stop offset="0" stop-color="#e8c35a"/>
          <stop offset="0.35" stop-color="#b8a45a"/>
          <stop offset="0.65" stop-color="#9fc040"/>
          <stop offset="1" stop-color="#6e9e22"/>
        </linearGradient>
        <radialGradient id="sunFlare" cx="0.15" cy="0.1" r="0.6">
          <stop offset="0" stop-color="#fff6cc" stop-opacity="0.9"/>
          <stop offset="1" stop-color="#fff6cc" stop-opacity="0"/>
        </radialGradient>
      </defs>

      <rect width="600" height="791" fill="var(--paper)"/>

      <g class="photo photo--hero" role="img" aria-label="Photograph of a smiling young woman sitting cross-legged on sunlit grass in a park">
        <rect x="0" y="150" width="600" height="460" fill="url(#meadowScene)"/>
        <rect x="0" y="150" width="600" height="460" fill="url(#sunFlare)"/>
      </g>

      <path class="header" d="M0 0 H600 V95 C430 150 240 190 0 190 Z" fill="var(--paper)"/>
      <path class="band band--gold" d="M0 190 C240 190 430 150 600 95 L600 108 C430 162 240 202 0 202 Z" fill="var(--gold)"/>

      <g class="brand brand--front" transform="translate(85 95) rotate(-2)">
        <circle cx="-14" cy="-10" r="9" fill="var(--gold)"/>
        <text class="brand-name" x="4" y="-14" font-size="36" fill="var(--charcoal-dark)">Clear Path</text>
        <text class="brand-name" x="6" y="20" font-size="28" fill="var(--charcoal-dark)">Psychology</text>
      </g>

      <g class="headline" transform="translate(70 290) rotate(-3)">
        <text x="0" y="0" fill="var(--paper)">WORKING TOGETHER</text>
        <text x="6" y="34" fill="var(--paper)">TO ACHIEVE A <tspan fill="#f3ead0">BETTER</tspan></text>
        <text x="12" y="66" fill="#efe6c6" fill-opacity="0.85">QUALITY OF LIFE</text>
      </g>

      <path class="band band--white" d="M0 560 C200 590 420 590 600 540 L600 560 C420 610 200 610 0 580 Z" fill="var(--paper)"/>
      <path class="footer" d="M0 580 C200 610 420 610 600 560 L600 791 L0 791 Z" fill="var(--charcoal)"/>
      <path class="band band--gold" d="M0 545 C200 575 420 575 600 525 L600 542 C420 592 200 592 0 562 Z" fill="var(--gold)"/>

      <g class="web" transform="translate(200 690) rotate(-3)">
        <circle cx="0" cy="-4" r="7" fill="none" stroke="var(--paper)" stroke-width="1.8"/>
        <path d="M-7 -4 H7 M0 -11 V3" stroke="var(--paper)" stroke-width="1.3"/>
        <text class="web-address" x="16" y="0">www.clearpathpsychology.com.au</text>
      </g>
    </svg>
  </section>

</main>
</body>
</html>
```